依頼詳細
現状、施工した場所に施工済ステッカーを貼っているのですが、
今回施工をしたホテル様の要望で、フロントや客室にお客様へ向けたアピールできるチラシなどが欲しいといわれました。
ホテルのフロント・客室の卓上におけるものや・車内に貼れるものなので
年賀状サイズくらいで検討しています。

イメージは
・主成分でもある青森ヒバをモチーフにしたもの
・一目でわかる安心感が伝わるもの
・100%天然成分で安心安全
・キャッチコピーは『植物の力で抗菌中!』

記載項目
ヴェルトナ産業株式会社 0120-387-905
Lumiva Plus
サイズ
年賀状サイズくらい
ページ数
片面
希望イメージ
シンプル 複雑
単色 カラフル
暗い 明るい
日常 高級
遊び心 厳粛
未来的 伝統的
女性的 男性的
希望する色
緑系、青系
納品ファイル
• 高解像度JPG (.jpg)
補足説明
当社が使用しているチラシです。
■ 選んだ理由

どの候補者もとても良かったですが、
こちらはどのシチュエーションでもあうようなデザインかつ
柔らかい印象で、安心感を与えてくれるようなデザインなので決めました。

■ 提案者全員のお礼・コメント

とても素晴らしいデザインばかりでかなり迷いました。
予算があれば他の候補者も当選sて他のですが。
今後は社のチラシなども作成予定ですので、
またお願いするかと思います。
宜しくお願い致します。

```html
<!DOCTYPE html>
<html lang="ja">
<head>
<meta charset="utf-8">
<title>植物の力で抗菌中！ ステッカー</title>
<link rel="stylesheet" href="https://fonts.googleapis.com/css2?family=M+PLUS+Rounded+1c:wght@500;800&family=Noto+Sans+JP:wght@400;500&display=swap">
<style>
  :root {
    --paper: #ffffff;
    --frame-line: #c9c9c9;
    --hiba-green: #2f8a43;
    --hiba-green-light: #5aa96a;
    --ink: #1f1f1f;
    --white: #ffffff;
  }
  * { margin: 0; padding: 0; box-sizing: border-box; }
  html, body {
    width: 900px;
    height: 1200px;
    overflow: hidden;
    background: var(--paper);
  }
  .sticker {
    position: relative;
    width: 900px;
    height: 1200px;
    background: var(--paper);
  }
  .sticker-frame {
    position: absolute;
    inset: 12px;
    border: 3px solid var(--frame-line);
  }
  .green-panel {
    position: absolute;
    left: 114px;
    top: 66px;
    width: 672px;
    height: 918px;
    background: var(--hiba-green);
    border-radius: 42px;
    color: var(--white);
    font-family: "M PLUS Rounded 1c", sans-serif;
    font-weight: 800;
    text-align: center;
  }
  .lead {
    position: absolute;
    left: 0;
    width: 100%;
    line-height: 1;
  }
  .lead-main-ingredient { top: 52px; font-size: 44px; letter-spacing: 2px; }
  .lead-natural { top: 110px; font-size: 42px; }
  .lead-plant-power { top: 172px; font-size: 70px; letter-spacing: 4px; }
  .hiba-leaf {
    position: absolute;
    left: 216px;
    top: 270px;
    width: 240px;
    height: 386px;
    border-radius: 120px 120px 40px 40px;
    background: linear-gradient(180deg, var(--hiba-green-light), var(--hiba-green));
  }
  .status-box {
    position: absolute;
    left: 24px;
    top: 642px;
    width: 624px;
    height: 252px;
    background: var(--white);
    border-radius: 0 0 26px 26px;
    display: flex;
    align-items: center;
    justify-content: center;
  }
  .status-text {
    color: var(--hiba-green);
    font-size: 116px;
    letter-spacing: 6px;
    line-height: 1;
  }
  .company {
    position: absolute;
    left: 0;
    width: 100%;
    text-align: center;
    font-family: "Noto Sans JP", sans-serif;
    color: var(--ink);
    line-height: 1;
  }
  .company-name { top: 1018px; font-size: 36px; font-weight: 500; }
  .company-contact { top: 1090px; font-size: 38px; font-weight: 400; }
  .company-contact .product { margin-right: 36px; }
</style>
</head>
<body>
  <main class="sticker">
    <div class="sticker-frame"></div>
    <section class="green-panel">
      <p class="lead lead-main-ingredient">青森ヒバ主成分</p>
      <p class="lead lead-natural">100%天然成分で安心安全</p>
      <h1 class="lead lead-plant-power">植物の力で</h1>
      <div class="hiba-leaf" role="img" aria-label="青森ヒバの葉のイラスト"></div>
      <div class="status-box">
        <p class="status-text">抗菌中!</p>
      </div>
    </section>
    <p class="company company-name">ヴェルトナ産業株式会社</p>
    <p class="company company-contact"><span class="product">Lumiva Plus</span><span class="phone">0120-387-905</span></p>
  </main>
</body>
</html>
```